Flyer-Design für Kreativwerkstatt
Zielgruppe
Kreativwerkstatt für Touristen - vorrangig Frauen
Aufgabenstellung
1 mal gefaltet
Wenn möglich außer dem Logo noch folgenden Text verwenden
Kreativität fängt da ,wo der Verstand aufhört das denken zu behindern

```html
<!DOCTYPE html>
<html lang="de">
<head>
<meta charset="utf-8">
<title>Lindenstube – Flyer</title>
<link href="https://fonts.googleapis.com/css2?family=Parisienne&display=swap" rel="stylesheet">
<style>
  :root {
    --backdrop: #6b4f3c;
    --orange-top: #f0921c;
    --orange-bottom: #d6600d;
    --cream: #f6e9c8;
    --cream-text: #fbe6c6;
    --brand-orange: #e0720f;
    --motif-tone: rgba(160, 70, 10, 0.28);
  }
  html, body {
    margin: 0;
    padding: 0;
    width: 1200px;
    height: 864px;
    overflow: hidden;
    background: var(--backdrop);
  }
  .canvas {
    position: relative;
    width: 1200px;
    height: 864px;
  }
  .flyer-cover {
    position: absolute;
    left: 395px;
    top: 22px;
    width: 410px;
    height: 820px;
    background: linear-gradient(170deg, var(--orange-top) 0%, #e57a14 45%, var(--orange-bottom) 100%);
    box-shadow: 0 6px 24px rgba(0, 0, 0, 0.35);
    overflow: hidden;
  }
  .brand-oval {
    position: absolute;
    left: 40px;
    top: 38px;
    width: 330px;
    height: 170px;
    border-radius: 50%;
    background: var(--cream);
    box-shadow: inset 0 0 10px rgba(150, 90, 30, 0.35);
    display: flex;
    align-items: center;
    justify-content: center;
  }
  .brand-oval::after {
    content: "";
    position: absolute;
    inset: 7px;
    border: 2px solid var(--brand-orange);
    border-radius: 50%;
  }
  .brand-name {
    font-family: "Parisienne", cursive;
    font-size: 58px;
    color: var(--brand-orange);
    margin: 0;
    font-weight: 400;
  }
  .quote {
    position: absolute;
    left: 0;
    right: 0;
    top: 290px;
    margin: 0;
    text-align: center;
    font-family: "Parisienne", cursive;
    font-size: 31px;
    line-height: 1.45;
    letter-spacing: 1px;
    color: var(--cream-text);
  }
  .motif {
    position: absolute;
    left: 45px;
    top: 500px;
    width: 320px;
    height: 260px;
    border-radius: 40% 40% 10% 10%;
    background: radial-gradient(ellipse at 55% 55%, var(--motif-tone) 0%, rgba(160, 70, 10, 0.12) 55%, rgba(160, 70, 10, 0) 75%);
  }
</style>
</head>
<body>
  <div class="canvas">
    <section class="flyer-cover">
      <div class="brand-oval">
        <p class="brand-name">Lindenstube</p>
      </div>
      <p class="quote">Kreativität fängt da an,<br>wo der Verstand aufhört<br>das Denken zu behindern</p>
      <div class="motif" role="img" aria-label="Dezentes Motiv: aufgeschlagenes Buch, aus dem Schmetterlinge auffliegen"></div>
    </section>
  </div>
</body>
</html>
```